Meridian Clearsound Wellness LLC Card Design

Need business card with a logo for a hearing aid sales and audiology business. We have two Hearing Instrument Specialists and one Audiologist on staff. Over 25 years in business. Locally owned and operated. Financing available. Most insurances accepted.

Meridian Clearsound Wellness LLC
48730 W Larkfield, Suite 9
Spokane, WA 99371
509-617-2084
www.meridianclearsound-example.com

Manager
Tobias Wrenfield HIS COHC
License #81957260

Target Market(s)

50yr old + people with a hearing loss.

Industry/Entity Type

Business

Contact Information for Business Card

48730 W Larkfield, Suite 9
Spokane, WA 99371
509-617-2084
www.meridianclearsound-example.com

Manager
Tobias Wrenfield HIS COHC
RTEQ #81957260

Font styles to use
Serif
Sans Serif

Requirements
Must have
• Business name, Tobias's name and title(s) and contact information, License #, web address
Nice to have
Should not have

```html
<!DOCTYPE html>
<html lang="en">
<head>
<meta charset="utf-8">
<title>Meridian Clearsound Wellness LLC – Business Card</title>
<link href="https://fonts.googleapis.com/css2?family=Jost:wght@300;400;600&family=Pathway+Gothic+One&display=swap" rel="stylesheet">
<style>
  :root {
    --backdrop-top: #d7dbe0;
    --backdrop-bottom: #eef0f2;
    --green-light: #2fb34b;
    --green-deep: #17a145;
    --ink: #ffffff;
    --rule: rgba(255, 255, 255, 0.55);
  }
  * { margin: 0; padding: 0; box-sizing: border-box; }
  html, body {
    width: 1200px;
    height: 746px;
    overflow: hidden;
  }
  body {
    background: linear-gradient(180deg, var(--backdrop-top), var(--backdrop-bottom));
    font-family: "Jost", "Futura", sans-serif;
    color: var(--ink);
    position: relative;
  }
  .card {
    position: absolute;
    left: 110px;
    top: 93px;
    width: 980px;
    height: 560px;
    background: var(--green-light);
    overflow: hidden;
    box-shadow: 0 10px 30px rgba(0, 0, 0, 0.18);
  }
  .card__band {
    position: absolute;
    left: 0;
    top: 160px;
    width: 100%;
    height: 250px;
    background: var(--green-deep);
    box-shadow: 0 -3px 6px rgba(0, 0, 0, 0.12), 0 3px 6px rgba(0, 0, 0, 0.12);
  }
  .brand {
    position: absolute;
    left: 60px;
    top: 58px;
    display: flex;
    align-items: center;
    gap: 14px;
  }
  .brand__dot {
    width: 34px;
    height: 34px;
    border: 3px solid var(--ink);
    border-radius: 50%;
  }
  .brand__name {
    font-weight: 300;
    font-size: 24px;
    line-height: 1.15;
    letter-spacing: 0.2px;
  }
  .person {
    position: absolute;
    left: 60px;
    top: 170px;
  }
  .person__first {
    font-weight: 600;
    font-size: 70px;
    line-height: 1;
  }
  .person__last {
    font-weight: 300;
    font-size: 46px;
    line-height: 1.15;
    margin-top: 2px;
  }
  .person__role,
  .person__license {
    font-weight: 400;
    font-size: 22px;
    line-height: 1.35;
  }
  .contact {
    position: absolute;
    left: 500px;
    top: 178px;
    width: 430px;
    list-style: none;
  }
  .contact__item {
    display: flex;
    align-items: flex-start;
    gap: 22px;
    padding: 14px 0;
    font-size: 22px;
    letter-spacing: 1px;
    line-height: 1.2;
  }
  .contact__item + .contact__item {
    border-top: 1px solid var(--rule);
  }
  .contact__icon {
    flex: none;
    width: 28px;
    height: 28px;
    fill: var(--ink);
  }
  .contact__text--web {
    font-size: 19px;
    letter-spacing: 0.5px;
    padding-top: 3px;
  }
  .company {
    position: absolute;
    left: 0;
    width: 100%;
    top: 440px;
    text-align: center;
    font-family: "Pathway Gothic One", "Arial Narrow", sans-serif;
    font-size: 50px;
    letter-spacing: 3px;
  }
</style>
</head>
<body>
  <article class="card">
    <div class="card__band"></div>

    <header class="brand">
      <span class="brand__dot"></span>
      <span class="brand__name">Meridian<br>Clearsound Wellness</span>
    </header>

    <section class="person">
      <h1 class="person__first">Tobias</h1>
      <p class="person__last">Wrenfield HIS COHC</p>
      <p class="person__role">Manager</p>
      <p class="person__license">License #81957260</p>
    </section>

    <ul class="contact">
      <li class="contact__item">
        <svg class="contact__icon" viewBox="0 0 24 24" aria-hidden="true">
          <path d="M2 8c0-2 4-4 10-4s10 2 10 4v2h-5V8.5c-1.5-.6-3.2-.9-5-.9s-3.5.3-5 .9V10H2z"/>
          <path d="M6 11h12l2 9H4z M12 13a2.5 2.5 0 1 0 0 5a2.5 2.5 0 1 0 0-5z"/>
        </svg>
        <span class="contact__text">509-617-2084</span>
      </li>
      <li class="contact__item">
        <svg class="contact__icon" viewBox="0 0 24 24" aria-hidden="true">
          <path fill="none" stroke="#fff" stroke-width="1.8" d="M12 2a10 10 0 1 0 0 20a10 10 0 1 0 0-20z M2 12h20 M12 2c-3 3-4 6.5-4 10s1 7 4 10 M12 2c3 3 4 6.5 4 10s-1 7-4 10 M4 6.5h16 M4 17.5h16"/>
        </svg>
        <span class="contact__text contact__text--web">www.meridianclearsound-example.com</span>
      </li>
      <li class="contact__item">
        <svg class="contact__icon" viewBox="0 0 24 24" aria-hidden="true">
          <path d="M12 1a8 8 0 0 0-8 8c0 6 8 14 8 14s8-8 8-14a8 8 0 0 0-8-8z M12 5.5a3.5 3.5 0 1 1 0 7a3.5 3.5 0 1 1 0-7z" fill-rule="evenodd"/>
        </svg>
        <span class="contact__text">48730 W Larkfield, Suite 9<br>Spokane, WA 99371</span>
      </li>
    </ul>

    <p class="company">Meridian Clearsound Wellness LLC</p>
  </article>
</body>
</html>
```